copper ridge construction website (squarespace build)

construction website - see attached documents

Target Market(s)

owners, cm's, and gc's

Coding

Coded - Design and coding required

Font styles to use
Serif

Colors
0054AA
0677BA
7BADD7
CADEEF
E8F1F8

```html
<!DOCTYPE html>
<html lang="en">
<head>
<meta charset="utf-8">
<title>Copper Ridge Construction</title>
<link href="https://fonts.googleapis.com/css2?family=Poppins:wght@400;500;600;700;800&display=swap" rel="stylesheet">
<style>
:root{
  --navy:#0b2657;
  --navy-deep:#08204b;
  --blue:#0677ba;
  --blue-strong:#0054aa;
  --sky:#7badd7;
  --mist:#cadeef;
  --ice:#e8f1f8;
  --gray:#a6a8ab;
  --steel:#6b6d70;
  --ink:#1d1d1f;
  --white:#ffffff;
}
*{box-sizing:border-box;margin:0;padding:0}
html,body{width:1200px;height:4412px;overflow:hidden}
body{position:relative;background:var(--white);font-family:'Poppins',sans-serif;color:var(--ink)}
.abs{position:absolute}
a{color:inherit;text-decoration:none}
.photo{position:absolute}
/* header */
.site-header{position:absolute;left:0;top:0;width:1200px;height:67px;background:var(--white)}
.brand{position:absolute;left:139px;top:17px;height:33px;display:flex;align-items:center;gap:8px;font-weight:700;font-size:20px;letter-spacing:1px;color:var(--navy)}
.brand-mark{width:14px;height:14px;background:var(--navy)}
.main-nav{position:absolute;top:27px;left:481px;font-size:10px;font-weight:600;color:var(--navy)}
.main-nav a{position:absolute;white-space:nowrap}
.main-nav .active{color:var(--blue)}
.caret{display:inline-block;width:5px;height:5px;border-right:1.5px solid currentColor;border-bottom:1.5px solid currentColor;transform:rotate(45deg);margin-left:4px;position:relative;top:-2px}
/* hero */
.hero{position:absolute;left:0;top:67px;width:1200px;height:613px;background:linear-gradient(90deg,#0d2d68,#12377a 60%,#1a4285)}
.hero-photo{left:590px;top:0;width:610px;height:613px;background:linear-gradient(160deg,#b8c2cc 0%,#6d7f96 35%,#2f4f86 65%,#1b3566 100%)}
.pile{position:absolute;background:var(--steel)}
.hero-title{position:absolute;left:139px;top:133px;font-size:55px;font-weight:800;line-height:56px;letter-spacing:.5px;color:var(--white)}
.hero-title .muted{color:var(--gray)}
.hero-text{position:absolute;left:139px;top:368px;width:340px;font-size:10.5px;line-height:16px;color:var(--white)}
.btn{position:absolute;display:flex;align-items:center;justify-content:center;background:var(--blue);color:var(--white);font-size:9.5px;font-weight:700;letter-spacing:.3px}
/* values */
.values{position:absolute;left:139px;top:742px;width:924px;display:flex;justify-content:space-between;align-items:center;font-size:14px;font-weight:700;color:var(--navy);letter-spacing:.3px}
.values svg{display:block}
/* headings */
.h2{font-weight:800;font-size:30px;color:var(--navy);line-height:1.05;letter-spacing:.2px}
.h2 .muted{color:var(--gray)}
.body-text{font-size:10.5px;line-height:15.6px;color:#2b2b2d}
/* about */
.about-photo{left:0;top:818px;width:620px;height:452px;background:linear-gradient(180deg,#a98457 0%,#b78d5f 40%,#a5714a 75%,#8f6140 100%)}
.dots{position:absolute;background:var(--mist);opacity:.8}
/* services */
.service-card{position:absolute;top:1426px;width:224px;height:360px}
.service-card .photo{left:0;top:0;width:224px;height:301px}
.service-label{position:absolute;left:0;top:301px;height:59px;display:flex;align-items:center;gap:12px;font-size:9.5px;font-weight:700;line-height:12px;color:var(--navy)}
.icon-box{width:55px;height:59px;background:var(--blue);display:flex;align-items:center;justify-content:center}
.services-note{position:absolute;left:0;top:1835px;width:1200px;text-align:center;font-size:10.5px;line-height:15.6px;color:#2b2b2d}
/* markets */
.markets{position:absolute;left:68px;top:1923px;width:1132px;height:565px;background:linear-gradient(120deg,#0c2a62,#0a2355)}
.markets-title{position:absolute;left:221px;top:2117px;font-size:28px;font-weight:800;line-height:33px;color:var(--white)}
.markets-title .muted{color:var(--gray)}
.markets-text{position:absolute;left:221px;top:2202px;width:360px;font-size:10.5px;line-height:15.6px;color:#e6ecf5}
.markets-kicker{position:absolute;left:637px;top:1997px;font-size:13px;font-weight:700;color:var(--white)}
.market{position:absolute;left:637px;width:400px;height:62px}
.market .icon-box{position:absolute;left:0;top:0;width:62px;height:62px;background:var(--steel);border:2px solid #c7c9cc}
.market h4{position:absolute;left:85px;top:6px;font-size:9.5px;font-weight:700;color:var(--white)}
.market p{position:absolute;left:85px;top:22px;width:270px;font-size:10.5px;line-height:14px;color:#e6ecf5}
/* why */
.why-photo{left:188px;top:2582px;width:394px;height:510px;background:linear-gradient(180deg,#9fb0c4 0%,#7b7f73 35%,#5e4b3a 65%,#6e6b62 100%)}
.why-title{position:absolute;left:642px;top:2712px;font-size:28px;font-weight:800;line-height:31px;color:var(--navy)}
.why-title .muted{color:var(--gray)}
/* projects */
.arrow-btn{position:absolute;top:3184px;width:41px;height:40px;display:flex;align-items:center;justify-content:center}
.arrow-btn span{width:9px;height:9px;border-left:2px solid var(--white);border-bottom:2px solid var(--white)}
.project-info{position:absolute;left:274px;top:3641px;width:361px;height:154px;background:var(--blue);padding:22px 0 0 30px;color:var(--white);font-size:10px;line-height:20px}
.project-info dl{display:grid;grid-template-columns:91px 1fr}
.project-info dt{font-weight:700}
/* footer */
.site-footer{position:absolute;left:0;top:3917px;width:1200px;height:495px;background:linear-gradient(120deg,#0d2c66,#0a2355)}
.newsletter-title{position:absolute;left:0;top:3976px;width:1140px;text-align:center;font-size:28px;font-weight:800;color:var(--white)}
.newsletter-title .muted{color:var(--gray)}
.news-input{position:absolute;left:294px;top:4027px;width:521px;height:39px;background:var(--white);display:flex;align-items:center;padding-left:18px;gap:10px;font-size:9.5px;color:#777}
.news-submit{position:absolute;left:815px;top:4027px;width:91px;height:39px;background:var(--blue);color:var(--white);font-size:10px;font-weight:700;display:flex;align-items:center;justify-content:center}
.footer-brand{position:absolute;left:202px;top:4168px;width:190px;font-size:26px;font-weight:600;line-height:30px;color:var(--white);letter-spacing:1px}
.footer-col h5{position:absolute;top:4135px;font-size:11px;font-weight:700;color:var(--white)}
.quick-links{position:absolute;left:450px;top:4165px;list-style:none;font-size:9.5px;line-height:18.5px;color:#e6ecf5}
.contact-item{position:absolute;left:611px;display:flex;gap:10px;color:#e6ecf5;font-size:9.5px;line-height:13px}
.contact-item b{display:block;font-size:9px;color:var(--white);font-weight:700}
.social{position:absolute;top:4170px;width:38px;height:38px;border:1px solid #3f5a8a;background:rgba(255,255,255,.06);display:flex;align-items:center;justify-content:center}
.social i{width:10px;height:10px;background:var(--white);opacity:.85}
.footer-rule{position:absolute;left:202px;top:4350px;width:800px;height:1px;background:#3b5384}
.copyright{position:absolute;left:202px;top:4373px;font-size:9.5px;font-weight:600;color:var(--white)}
.legal{position:absolute;left:803px;top:4373px;font-size:9.5px;color:#e6ecf5;display:flex;gap:10px}
</style>
</head>
<body>

<header class="site-header">
  <div class="brand"><span class="brand-mark"></span>COPPER RIDGE</div>
  <nav class="main-nav">
    <a class="active" style="left:0">HOME</a>
    <a style="left:62px">ABOUT US</a>
    <a style="left:144px">OUR SERVICES<span class="caret"></span></a>
    <a style="left:247px">PROJECT PORTFOLIO<span class="caret"></span></a>
    <a style="left:380px">MARKET INDUSTRIES<span class="caret"></span></a>
    <a style="left:517px">CONTACT US</a>
  </nav>
</header>

<section class="hero">
  <div class="photo hero-photo" role="img" aria-label="Workers walking along a row of steel wall forms on a construction site"></div>
  <div class="pile" role="img" aria-label="Helical pile graphic" style="left:551px;top:0;width:96px;height:613px;background:linear-gradient(90deg,transparent 35px,var(--steel) 35px,var(--steel) 61px,transparent 61px)"></div>
  <h1 class="hero-title">BUILDING<br><span class="muted">EXCELLENCE</span><br>THROUGH<br><span class="muted">EXPERIENCE</span></h1>
  <p class="hero-text">Copper Ridge Construction is a self-performing foundation and geo technical general contractor and the critical first phase of every successful project.</p>
  <a class="btn" style="left:139px;top:439px;width:170px;height:35px">VIEW OUR SERVICES</a>
</section>

<div class="values">
  <span>SAFETY</span><svg width="16" height="16" viewBox="0 0 16 16" stroke="#0677ba" stroke-width="2.4" stroke-linecap="round"><path d="M8 1v14M2 4.5l12 7M2 11.5l12-7"/></svg>
  <span>PERFORMANCE</span><svg width="16" height="16" viewBox="0 0 16 16" stroke="#0677ba" stroke-width="2.4" stroke-linecap="round"><path d="M8 1v14M2 4.5l12 7M2 11.5l12-7"/></svg>
  <span>QUALITY</span><svg width="16" height="16" viewBox="0 0 16 16" stroke="#0677ba" stroke-width="2.4" stroke-linecap="round"><path d="M8 1v14M2 4.5l12 7M2 11.5l12-7"/></svg>
  <span>EXPERIENCE</span><svg width="16" height="16" viewBox="0 0 16 16" stroke="#0677ba" stroke-width="2.4" stroke-linecap="round"><path d="M8 1v14M2 4.5l12 7M2 11.5l12-7"/></svg>
  <span>INTEGRITY</span><svg width="16" height="16" viewBox="0 0 16 16" stroke="#0677ba" stroke-width="2.4" stroke-linecap="round"><path d="M8 1v14M2 4.5l12 7M2 11.5l12-7"/></svg>
  <span>CRAFTSMEN</span>
</div>

<section class="about">
  <div class="photo about-photo" role="img" aria-label="Excavated foundation pit lined with timber lagging"></div>
  <div class="dots" role="img" aria-label="Dot grid accent" style="left:625px;top:1207px;width:12px;height:77px"></div>
  <div class="dots" style="left:551px;top:1272px;width:80px;height:12px"></div>
  <h2 class="h2 abs" style="left:690px;top:896px">ABOUT <span class="muted">US</span></h2>
  <p class="body-text abs" style="left:690px;top:938px;width:356px"><b>Copper Ridge Construction</b> is a self-performing foundation and geotechnical general contractor and the critical first phase of every successful project.</p>
  <p class="body-text abs" style="left:690px;top:1001px;width:356px">Copper Ridge partners with owners, construction managers, and general contractors from design through construction delivery. Our team supports projects at every phase — preconstruction, engineering and design support, exploratory investigations, design proof testing, and complete structural packages for our clients. Copper Ridge brings precision, accountability, and true partnership to ground-level work — because what's below the surface determines everything above it.</p>
  <a class="btn" style="left:690px;top:1150px;width:171px;height:36px">FIND OUT MORE</a>
</section>

<section class="services">
  <h2 class="h2 abs" style="left:0;top:1372px;width:1200px;text-align:center">OUR <span class="muted">SERVICES</span></h2>

  <article class="service-card" style="left:130px">
    <div class="photo" role="img" aria-label="Crew members inspecting a site beside a pink insulated wall" style="background:linear-gradient(180deg,#c98a9c 0%,#8a6a74 45%,#4a4f5e 80%,#6a6d72 100%)"></div>
    <div class="service-label"><span class="icon-box"><svg width="26" height="26" viewBox="0 0 26 26" fill="#fff"><circle cx="13" cy="8" r="5"/><path d="M3 25c0-6 4-10 10-10s10 4 10 10z"/></svg></span>OWNER, CM'S, &amp;<br>GC'S SERVICES</div>
  </article>
  <article class="service-card" style="left:368px">
    <div class="photo" role="img" aria-label="Excavation with formwork and earth retention walls" style="background:linear-gradient(180deg,#8b9a80 0%,#9b8364 40%,#4c4f55 70%,#b07a72 100%)"></div>
    <div class="service-label"><span class="icon-box"><svg width="26" height="26" viewBox="0 0 26 26" fill="#fff"><rect x="2" y="14" width="10" height="10"/><rect x="14" y="14" width="10" height="10"/><rect x="8" y="3" width="10" height="9"/></svg></span>FOUNDATION &amp;<br>EARTH RETENTION</div>
  </article>
  <article class="service-card" style="left:608px">
    <div class="photo" role="img" aria-label="Reinforced concrete foundation walls over gravel" style="background:linear-gradient(180deg,#6f6e6a 0%,#9a9893 40%,#7e7b74 70%,#9c968b 100%)"></div>
    <div class="service-label"><span class="icon-box"><svg width="28" height="26" viewBox="0 0 28 26" fill="#fff"><rect x="2" y="6" width="11" height="7"/><rect x="15" y="6" width="11" height="7"/><rect x="8" y="15" width="12" height="7"/></svg></span>REINFORCED CONCRETE,<br>MASONRY, &amp; OTHER</div>
  </article>
  <article class="service-card" style="left:846px">
    <div class="photo" role="img" aria-label="Concrete building frame under construction with yellow shoring" style="background:linear-gradient(180deg,#b9cfe3 0%,#c7c2a3 40%,#a89f84 70%,#8a8577 100%)"></div>
    <div class="service-label"><span class="icon-box"><svg width="26" height="26" viewBox="0 0 26 26" fill="#fff"><path d="M5 11a8 8 0 0 1 16 0z"/><rect x="4" y="12" width="18" height="2"/><rect x="7" y="16" width="12" height="9"/></svg></span>ENGINEERING &amp;<br>DESIGN SUPPORT</div>
  </article>

  <p class="services-note">shoring, ground improvement, or reinforced concrete — Copper Ridge self-performs the work with<br>dedicated crews, modern equipment, and engineering-driven means and methods.</p>
</section>

<section>
  <div class="markets"></div>
  <div class="pile" role="img" aria-label="Helical pile graphic" style="left:43px;top:1923px;width:89px;height:565px;background:linear-gradient(90deg,transparent 32px,var(--steel) 32px,var(--steel) 56px,transparent 56px)"></div>
  <h2 class="markets-title">MARKETS AND<br><span class="muted">INDUSTRIES</span></h2>
  <p class="markets-text">Copper Ridge Construction serves owners, construction managers, and general contractors and subcontractors across the New York, New Jersey, and Connecticut tri-state region. Our self-performing model allows us to support projects of every scale and complexity throughout the region.</p>
  <h3 class="markets-kicker">MARKETS WE SERVE</h3>

  <div class="market" style="top:2037px"><span class="icon-box"><svg width="28" height="30" viewBox="0 0 28 30" fill="#fff"><rect x="4" y="4" width="12" height="24"/><rect x="17" y="12" width="8" height="16"/></svg></span><h4>COMMERCIAL</h4><p>Office, retail, and mixed-use foundation and structural packages.</p></div>
  <div class="market" style="top:2116px"><span class="icon-box"><svg width="28" height="28" viewBox="0 0 28 28" fill="#fff"><path d="M14 3 2 14h4v11h16V14h4z"/></svg></span><h4>RESIDENTIAL</h4><p>Multi-family and single-family foundation, underpinning, and earth-retention work.</p></div>
  <div class="market" style="top:2195px"><span class="icon-box"><svg width="28" height="28" viewBox="0 0 28 28" fill="#fff"><path d="M3 26V13l7 4v-4l7 4V5h6v21z"/></svg></span><h4>INDUSTRIAL</h4><p>Warehouse and distribution center foundation systems, including complete structural packages.</p></div>
  <div class="market" style="top:2273px"><span class="icon-box"><svg width="30" height="28" viewBox="0 0 30 28" fill="#fff"><circle cx="15" cy="8" r="5"/><circle cx="7" cy="16" r="3"/><circle cx="23" cy="16" r="3"/><path d="M3 26c0-4 2-6 4-6s4 2 4 6zM19 26c0-4 2-6 4-6s4 2 4 6zM10 26c0-5 2-8 5-8s5 3 5 8z"/></svg></span><h4>PUBLIC WORKS &amp; INFRASTRUCTURE</h4><p>Municipal, transportation, and public agency projects.</p></div>
  <div class="market" style="top:2354px"><span class="icon-box"><svg width="28" height="28" viewBox="0 0 28 28" fill="#fff"><path d="M14 2 4 8h20z"/><rect x="5" y="10" width="18" height="16"/></svg></span><h4>INSTITUTIONAL</h4><p>Healthcare, education, and government facility foundation work.</p></div>
</section>

<section class="why">
  <div class="photo why-photo" role="img" aria-label="Drill rig installing piles on an urban job site"></div>
  <div class="dots" role="img" aria-label="Dot grid accent" style="left:168px;top:3022px;width:12px;height:85px"></div>
  <div class="dots" style="left:168px;top:3095px;width:85px;height:12px"></div>
  <h2 class="why-title">WHY OWNERS,<br>CMS, &amp; GCS CHOOSE<br><span class="muted">COPPER RIDGE</span></h2>
  <p class="body-text abs" style="left:642px;top:2824px;width:361px">Foundation and geotechnical work sets the tone for the project and every phase that follows. Copper Ridge brings a self-performing, safety-first, engineering-informed approach to every market we serve — helping project teams de-risk the ground-level phase of construction through constructability review, value engineering, and disciplined field execution.</p>
  <p class="body-text abs" style="left:642px;top:2934px;width:361px">Whether the project calls for helical piles on a residential lot or a full earth-retention and deep-foundation package on a commercial high-rise, Copper Ridge delivers the same standard: precision, accountability, and true partnership from the ground up.</p>
</section>

<section class="projects">
  <h2 class="h2 abs" style="left:0;top:3196px;width:1200px;text-align:center">PROJECT <span class="muted">PROFILES</span></h2>
  <a class="arrow-btn" style="left:974px;background:var(--navy)"><span style="transform:rotate(45deg);margin-left:4px"></span></a>
  <a class="arrow-btn" style="left:1020px;background:#b3b5b8"><span style="transform:rotate(-135deg);margin-right:4px"></span></a>
  <div class="photo" role="img" aria-label="Concrete high-rise frame with yellow shoring" style="left:0;top:3261px;width:207px;height:459px;background:linear-gradient(180deg,#8c8a83 0%,#6d6a62 50%,#4a4741 100%)"></div>
  <div class="photo" role="img" aria-label="Large foundation excavation with retaining walls and workers" style="left:221px;top:3261px;width:757px;height:459px;background:linear-gradient(180deg,#98a293 0%,#a4a39a 30%,#8d7660 60%,#a26e55 100%)"></div>
  <div class="photo" role="img" aria-label="Completed brick multi-family residential building" style="left:989px;top:3261px;width:211px;height:459px;background:linear-gradient(180deg,#c3c9d0 0%,#9da3a8 35%,#8f5a47 65%,#6f4a3d 100%)"></div>
  <div class="project-info">
    <dl>
      <dt>PROJECT:</dt><dd>Manhattan Skyscraper Foundation.</dd>
      <dt>DESCRIPTION:</dt><dd>Helical pile installation and retaining wall.</dd>
      <dt>VALUE:</dt><dd>$5.2 Million</dd>
      <dt>CLIENT:</dt><dd>Harborline Developments</dd>
      <dt>STAN OUTS:</dt><dd>Completed 3 weeks ahead of schedule</dd>
    </dl>
  </div>
</section>

<footer class="site-footer"></footer>
<div class="pile" role="img" aria-label="Helical pile graphic" style="left:1082px;top:3917px;width:79px;height:495px;background:linear-gradient(90deg,transparent 28px,var(--steel) 28px,var(--steel) 51px,transparent 51px)"></div>
<h2 class="newsletter-title">SUBSCRIBE <span class="muted">NEWSLETTER</span></h2>
<div class="news-input"><svg width="11" height="8" viewBox="0 0 11 8"><rect x=".5" y=".5" width="10" height="7" fill="none" stroke="#999"/><path d="M.5 .5 5.5 4.5 10.5 .5" fill="none" stroke="#999"/></svg>Enter your email address</div>
<a class="news-submit">SUBMIT</a>

<div class="footer-brand">COPPER<br>RIDGE</div>

<div class="footer-col">
  <h5 style="left:450px">QUICK LINKS</h5>
  <ul class="quick-links">
    <li>Home</li><li>About Us</li><li>Our Services</li><li>Project Portfolio</li><li>Market Industries</li><li>Contact</li>
  </ul>
  <h5 style="left:611px">CONTACT US</h5>
  <div class="contact-item" style="top:4168px"><svg width="12" height="12" viewBox="0 0 12 12" fill="#3c8fd0"><path d="M2 1h3l1 3-2 1a7 7 0 0 0 3 3l1-2 3 1v3c-6 1-10-3-9-9z"/></svg><div><b>PHONE</b>+123-456-789</div></div>
  <div class="contact-item" style="top:4206px"><svg width="12" height="10" viewBox="0 0 12 10" fill="#3c8fd0"><rect width="12" height="9" rx="1"/></svg><div><b>EMAIL</b>info@copperridge.com</div></div>
  <div class="contact-item" style="top:4244px"><svg width="12" height="14" viewBox="0 0 12 14" fill="#3c8fd0"><path d="M6 0a5 5 0 0 1 5 5c0 4-5 9-5 9S1 9 1 5a5 5 0 0 1 5-5z"/><circle cx="6" cy="5" r="2" fill="#0b2657"/></svg><div><b>ADDRESS</b>88 Foundry Lane, Suite<br>210, Hudson, NY 12534</div></div>
  <h5 style="left:796px">FOLLOW US</h5>
  <a class="social" style="left:796px" aria-label="Social profile 1"><i></i></a>
  <a class="social" style="left:842px" aria-label="Social profile 2"><i></i></a>
  <a class="social" style="left:888px" aria-label="Social profile 3"><i></i></a>
  <a class="social" style="left:934px" aria-label="Social profile 4"><i></i></a>
</div>

<div class="footer-rule"></div>
<p class="copyright">© COPYRIGHT 2026 ALL RIGHTS RESERVED</p>
<p class="legal"><span>Terms &amp; Condition</span><span>|</span><span>Privacy Policy</span></p>

</body>
</html>
```